Corporate Branding - Web and Print

A UK based company will like to use an existing logo to create branding materials for all marketing related documents, including business card, prints, letterhead, Website, Twitter, Facebook, Instagram logo etc. This company serves high-end clientele in the fashion, health and wellness and as such high quality and class is of utmost importance.
Where the logo can be modernised without losing its character then experiment. The main thing is to have a corporate branding which can be used later for brochures, Business Plan infographics.
The prominent colour within the organisation is burnt orange with no secondary colour. However if you believe a secondary colour is needed then use it, otherwise keep it simple and classy. Any chosen colours have to match perfectly.
Target Market(s)
High net worth individuals
Industry/Entity Type
Health And Wellness
Contact Information for Business Card
classy
Look and feel
Each slider illustrates characteristics of the customer's brand and the style your logo design should communicate.

```html
<!DOCTYPE html>
<html lang="en">
<head>
<meta charset="utf-8">
<title>Veloria Business Card</title>
<link rel="stylesheet" href="https://fonts.googleapis.com/css2?family=EB+Garamond:wght@400;600;700&display=swap">
<style>
  :root {
    --burnt-orange: #e08a1e;
    --burnt-orange-deep: #b86a12;
    --charcoal: #262626;
    --card-dark: #2e2e2e;
    --card-dark-edge: #1f1f1f;
    --paper: #f4f4f4;
    --swoosh-grey: #a9a9a9;
    --ink: #1c1c1c;
    --backdrop: #333333;
  }
  * { margin: 0; padding: 0; box-sizing: border-box; }
  html, body { width: 1200px; height: 997px; overflow: hidden; }
  body {
    background: var(--backdrop);
    font-family: "EB Garamond", Georgia, serif;
    position: relative;
  }
  .card {
    position: absolute;
    left: 250px;
    width: 700px;
    height: 400px;
    border-radius: 4px;
    overflow: hidden;
    box-shadow: 0 10px 30px rgba(0,0,0,.45);
  }
  /* Back side */
  .card-back { top: 54px; }
  .card-back .texture {
    position: absolute; inset: 0;
    background: linear-gradient(135deg, var(--card-dark) 0%, var(--card-dark-edge) 100%);
  }
  .card-back .brand {
    position: absolute; left: 0; right: 0; top: 160px;
    display: flex; align-items: center; justify-content: center; gap: 22px;
  }
  .card-back .brand-dot {
    width: 62px; height: 62px; border-radius: 50%; background: #ffffff;
  }
  .card-back .brand-name {
    color: #ffffff; font-weight: 700; font-size: 76px; letter-spacing: 4px; line-height: 1;
  }
  .card-back .web {
    position: absolute; right: 34px; bottom: 26px;
    color: #bdbdbd; font-size: 15px; letter-spacing: 2px;
  }
  /* Front side */
  .card-front { top: 514px; background: var(--paper); }
  .card-front .brand {
    position: absolute; left: 56px; top: 120px;
    display: flex; align-items: center; gap: 14px;
  }
  .card-front .brand-dot {
    width: 40px; height: 40px; border-radius: 50%; background: var(--burnt-orange);
  }
  .card-front .brand-name {
    color: var(--burnt-orange); font-weight: 700; font-size: 52px; letter-spacing: 2px; line-height: 1;
  }
  .divider {
    position: absolute; left: 372px; top: 30px; width: 2px; height: 220px;
    background: linear-gradient(to bottom, rgba(224,138,30,0), var(--burnt-orange) 25%, var(--burnt-orange) 70%, rgba(224,138,30,0));
  }
  .contact { position: absolute; left: 400px; top: 38px; color: var(--ink); }
  .contact .person { color: var(--burnt-orange); font-weight: 600; font-size: 21px; line-height: 1.1; }
  .contact .role { font-size: 13px; margin-bottom: 14px; }
  .contact ul { list-style: none; }
  .contact li { display: flex; align-items: center; gap: 10px; font-size: 15px; height: 28px; }
  .icon {
    width: 20px; height: 20px; border-radius: 50%; background: var(--burnt-orange);
    display: flex; align-items: center; justify-content: center; flex: none;
  }
  .icon svg { width: 11px; height: 11px; fill: #ffffff; }
  .contact address {
    font-style: normal; color: var(--burnt-orange); font-size: 16px; line-height: 1.25; margin-top: 10px;
  }
  .footer-band { position: absolute; left: 0; bottom: 0; width: 700px; height: 400px; }
</style>
</head>
<body>

  <section class="card card-back" aria-label="Business card back">
    <div class="texture" role="img" aria-label="Dark faceted geometric background"></div>
    <div class="brand">
      <span class="brand-dot"></span>
      <span class="brand-name">VELORIA</span>
    </div>
    <span class="web">veloria.com</span>
  </section>

  <section class="card card-front" aria-label="Business card front">
    <svg class="footer-band" viewBox="0 0 700 400" aria-hidden="true">
      <path d="M170 318 C 400 300, 590 255, 700 182 L700 198 C 590 270, 400 312, 170 320 Z" fill="var(--swoosh-grey)"/>
      <path d="M0 350 C 260 338, 540 300, 700 212 L700 400 L0 400 Z" fill="var(--burnt-orange)"/>
    </svg>

    <div class="brand">
      <span class="brand-dot"></span>
      <span class="brand-name">VELORIA</span>
    </div>

    <div class="divider"></div>

    <div class="contact">
      <p class="person">Harlan Pryce</p>
      <p class="role">Owner / Founder</p>
      <ul>
        <li><span class="icon"><svg viewBox="0 0 24 24"><path d="M6.6 10.8c1.4 2.8 3.8 5.1 6.6 6.6l2.2-2.2c.3-.3.7-.4 1-.2 1.1.4 2.3.6 3.6.6.6 0 1 .4 1 1V20c0 .6-.4 1-1 1C10.6 21 3 13.4 3 4c0-.6.4-1 1-1h3.5c.6 0 1 .4 1 1 0 1.3.2 2.5.6 3.6.1.3 0 .7-.2 1z"/></svg></span>503-555-0142</li>
        <li><span class="icon"><svg viewBox="0 0 24 24"><path d="M6 3h10l2 2v4H6zM4 10h16a2 2 0 0 1 2 2v6h-4v3H6v-3H2v-6a2 2 0 0 1 2-2zm4 6v3h8v-3z"/></svg></span>1-877-555-0199</li>
        <li><span class="icon"><svg viewBox="0 0 24 24"><path d="M3 5h18v14H3zm2 2v.5l7 4.5 7-4.5V7zm0 2.8V17h14V9.8l-7 4.5z"/></svg></span>harlan@veloriastudio.com</li>
      </ul>
      <address>2210 Alder Lane NW,<br>Portland, OR 97210</address>
    </div>
  </section>

</body>
</html>
```